ZiPU Vortal Bhutan Trip

This is a one-page (A5) flyer to attract sign ups for Bhutan Trip.

Target Market(s)

Young entrepreneurs (worldwide)

Requirements
Must have
• Must have "WOW" effect and attract sign ups
Nice to have
• Striking and vibrant

```html
<!DOCTYPE html>
<html lang="en">
<head>
<meta charset="utf-8">
<title>ZiPU Vortal Bhutan Trip</title>
<link rel="stylesheet" href="https://fonts.googleapis.com/css2?family=Oswald:wght@500;600&family=Montserrat:ital,wght@1,500&family=Lato:wght@400;700&display=swap">
<style>
  :root {
    --page-bg: #d8d8d8;
    --paper: #f4f4f4;
    --ink: #1f1f1f;
    --red: #e8232b;
    --blue: #0aa6d9;
    --magenta: #c5168c;
    --lime: #a6cc2a;
    --yellow: #f4c51a;
    --frame-red: #ef4a47;
    --ring-grey: #9a9a9a;
  }
  * { box-sizing: border-box; margin: 0; padding: 0; }
  html, body { width: 1200px; height: 1200px; overflow: hidden; }
  body { background: var(--page-bg); position: relative; font-family: "Lato", sans-serif; }

  .flyer {
    position: absolute; left: 191px; top: 20px;
    width: 834px; height: 1183px;
    transform: scale(0.98); transform-origin: top left;
    background: linear-gradient(180deg, #ffffff 0%, var(--paper) 60%, #e9e9e9 100%);
    overflow: hidden;
  }
  .abs { position: absolute; }

  .brand { left: 78px; top: 70px; display: flex; align-items: center; gap: 12px;
    font-family: "Lato", sans-serif; font-weight: 700; font-size: 46px; color: var(--ink); }
  .brand-dot { width: 20px; height: 20px; border-radius: 50%; background: var(--magenta); }

  .title { left: 74px; top: 232px; font-family: "Oswald", sans-serif; font-weight: 600;
    line-height: 1.08; text-transform: uppercase; }
  .title .t1 { font-size: 48px; color: var(--ink); }
  .title .t2 { font-size: 60px; color: var(--red); }
  .title .t3 { font-size: 54px; color: var(--ink); }

  .swoosh { left: 0; top: 380px; }

  .photo-frame { left: 435px; top: 74px; width: 331px; height: 566px;
    border: 5px solid var(--frame-red); background: #fff; box-shadow: 0 8px 18px rgba(0,0,0,.2); }
  .photo { width: 100%; }
  .photo-temple { height: 298px; background: linear-gradient(180deg, #7fa8cf 0%, #c9d6e2 35%, #a8604a 55%, #b8a58c 100%); }
  .photo-dzong { height: 256px; margin-top: 2px; background: linear-gradient(180deg, #e7ecef 0%, #4f7a45 35%, #9a4a3c 60%, #e8e4dc 100%); }

  .tagline { left: 66px; top: 582px; font-family: "Montserrat", sans-serif; font-style: italic;
    font-weight: 500; font-size: 23px; line-height: 29px; color: var(--ink); }
  .tagline em { color: var(--red); font-style: italic; }

  .photo-bridge { left: 51px; top: 710px; width: 356px; height: 150px; border: 5px solid var(--lime);
    background: linear-gradient(180deg, #3f6f33 0%, #6d9a4e 45%, #b9b4a6 80%, #7d8b6e 100%);
    box-shadow: 0 8px 14px rgba(0,0,0,.15); }

  .highlights-tag { left: 675px; top: 686px; width: 170px; height: 35px; border-radius: 18px 0 0 18px;
    background: var(--magenta); color: #fff; font-weight: 700; font-size: 17px; line-height: 35px; padding-left: 19px; }
  .highlights { right: 57px; top: 730px; list-style: none; text-align: right; font-size: 15.5px; line-height: 19.2px; color: var(--ink); }
  .highlights li::after { content: ""; display: inline-block; width: 8px; height: 8px; border-radius: 50%;
    background: var(--magenta); margin-left: 8px; vertical-align: middle; }

  .price { left: 62px; top: 898px; }
  .price-label { font-family: "Oswald", sans-serif; font-weight: 600; font-size: 34px; line-height: 38px; color: var(--ink); }
  .price-main { font-family: "Oswald", sans-serif; font-weight: 500; font-size: 34px; line-height: 38px; color: var(--blue); }
  .price-note { font-size: 11px; color: var(--ink); margin-top: 6px; }
  .price-early { font-size: 23px; line-height: 24px; color: var(--red); }

  .circle { border-radius: 50%; background: #fff; display: flex; align-items: center; justify-content: center;
    text-align: center; box-shadow: 0 0 0 6px var(--ring-grey); }
  .partner-left { left: 284px; top: 908px; width: 190px; height: 190px; border: 8px solid var(--lime); }
  .partner-right { left: 641px; top: 934px; width: 176px; height: 176px; border: 8px solid var(--lime); }
  .partner-name { font-weight: 700; font-size: 18px; color: #1c4f86; }
  .partner-right .partner-name { color: #1e8fb0; }
  .photo-fort { left: 446px; top: 886px; width: 220px; height: 220px; border: 8px solid #f3e6ee;
    background: linear-gradient(180deg, #3b86d6 0%, #9cc3ea 40%, #e6e2da 60%, #3f6b2e 100%); }

  .footer-band { left: 0; top: 1050px; }
  .footer-text { left: 0; right: 0; top: 1122px; text-align: center; color: #fff; font-weight: 700; font-size: 21.5px; }
</style>
</head>
<body>
<main class="flyer">
  <div class="brand abs"><span>ZiPU Vortal</span><span class="brand-dot"></span></div>

  <h1 class="title abs">
    <div class="t1">ZiPU Vortal</div>
    <div class="t2">Bhutan Trip</div>
    <div class="t3">3-6 July 2017</div>
  </h1>

  <svg class="swoosh abs" width="834" height="200" viewBox="0 0 834 200">
    <path d="M0,35 C180,125 420,170 834,25 L834,90 C500,220 200,180 0,115 Z" fill="var(--blue)"/>
    <path d="M0,35 C180,125 420,170 834,25 L834,40 C440,180 180,140 0,50 Z" fill="#ffffff"/>
  </svg>

  <div class="photo-frame abs">
    <div class="photo photo-temple" role="img" aria-label="Monk in red robe walking toward a Bhutanese temple"></div>
    <div class="photo photo-dzong" role="img" aria-label="Large Bhutanese dzong with green mountains behind"></div>
  </div>

  <p class="tagline abs">Sign up for a once in a<br><em>lifetime experience in</em><br>the land of happiness!</p>

  <div class="photo-bridge abs" role="img" aria-label="Chain bridge with prayer flags leading to a small temple in green hills"></div>

  <div class="highlights-tag abs">Highlights</div>
  <ul class="highlights abs">
    <li>LEARN from Leading Social Change Makers</li>
    <li>ENGAGE the community through volunteering</li>
    <li>DISCOVER your inner happiness</li>
    <li>SAVOUR Organic food</li>
    <li>IMMERSE in traditional sports and craft</li>
    <li>EXPERIENCE warm Bhutanese hospitality</li>
    <li>REJUVENATE your mind, body and soul</li>
  </ul>

  <div class="price abs">
    <div class="price-label">PRICE AT</div>
    <div class="price-main">USD2800</div>
    <div class="price-note">Early bird discount</div>
    <div class="price-early">USD2300</div>
    <div class="price-note" style="margin-top:0">(If you sign up by 31 March 2017)</div>
  </div>

  <svg class="footer-band abs" width="834" height="133" viewBox="0 0 834 133">
    <path d="M0,48 Q417,-5 834,45 L834,133 L0,133 Z" fill="var(--yellow)"/>
    <path d="M0,56 Q417,3 834,53 L834,133 L0,133 Z" fill="var(--ink)"/>
  </svg>

  <div class="circle partner-left abs"><span class="partner-name">Banyan Circle</span></div>
  <div class="circle partner-right abs"><span class="partner-name">Yakpath Tours</span></div>
  <div class="circle photo-fort abs" role="img" aria-label="White Bhutanese fortress on a forested hill under blue sky"></div>

  <p class="footer-text abs">Register now! Limited to 30 participants! | Email: ravi@kindlefund.sg</p>
</main>
</body>
</html>
```